CalmPath Nurses' Manifesto

Design a manifesto to inspire and motivate nurses to work at minimum standards of excellence in their nursing practice.

The manifesto will become a feature of our website, at conferences, workshops and retreats. It will also be featured on other marketing tools.

Primary Market:
Nurses and/or other healthcare professionals (specifically Doctors, Occupational Therapists, Psychologists and Social Workers).

However the manifesto is equally applicable to all nurses and healthcare professionals from new graduates to very experienced senior clinicians, administration officers,managers and healthcare executive personnel.

Mainly females and primarily 35 to 65 years old, which suggests people in this target age group have extensive experience, but have become jaded'.

The purpose of our business is to assist healthcare professionals, primarily nurses, to maintain their enthusiasm and excellence in service provision, for their benefit as well as the benefit of the clients.

I have attached:
File 1: Copy Samples and examples: which has the copy for the manifesto, examples that appeal to us and our 3 attempts.
File 2: Our colour Spec Sheet, HOWEVER the colours are not necessary limited to these colours. These colours are not in the logo that will be on the manifesto. The colours on the logo attached can/or also be used.
File 3: Prototype logo. The final logo will be available within 3 to 4 days.

Requirements
Must have
• Must use the copy as per the attached file.

It should be contemporary, eye catching and motivational.

Sample 1 on the attached file (File 3: copy, samples and examples_554207 saturday, 29 june 2013 06:24:3030) Is close to what we are looking for.
Should not have
• MUST BE EASY TO READ. Each line MUST be clearly defined from each other.

```html
<!DOCTYPE html>
<html lang="en">
<head>
<meta charset="utf-8">
<title>CalmPath Nurses' Manifesto</title>
<link rel="stylesheet" href="https://fonts.googleapis.com/css2?family=Bebas+Neue&family=Oswald:wght@400;600&family=Playfair+Display:ital,wght@1,700&family=Dancing+Script:wght@700&display=swap">
<style>
  :root {
    --sky-top: #0a1626;
    --sky-mid: #1d344d;
    --horizon: #6d7680;
    --dusk: #9a8570;
    --road: #232325;
    --white: #ffffff;
    --orange: #f7941d;
    --cream: #fbe3b6;
    --condensed: 'Bebas Neue', 'Oswald', sans-serif;
    --sans: 'Oswald', sans-serif;
    --serif: 'Playfair Display', serif;
    --script: 'Dancing Script', cursive;
  }
  html, body { margin: 0; padding: 0; overflow: hidden; background: var(--sky-top); }
  .poster { position: relative; width: 849px; height: 1200px; overflow: hidden; }
  .backdrop {
    position: absolute; inset: 0;
    background: linear-gradient(180deg, var(--sky-top) 0%, var(--sky-mid) 40%, var(--horizon) 62%, var(--dusk) 68%, #4a4640 74%, var(--road) 100%);
  }
  .title-banner {
    position: absolute; margin: 0; left: 147px; top: 74px; width: 546px; height: 50px;
    background: var(--orange);
    display: flex; align-items: center; justify-content: center;
    font-family: var(--condensed); font-weight: 400; font-size: 54px; color: var(--white);
    letter-spacing: 2px; line-height: 1; padding-top: 4px; box-sizing: border-box;
  }
  .line {
    position: absolute; margin: 0; white-space: nowrap; line-height: 1;
    font-family: var(--condensed); color: var(--white);
  }
  .small { font-family: var(--sans); font-weight: 400; letter-spacing: .2px; }
  .accent { color: var(--orange); }
  .cream { color: var(--cream); }
  .script { font-family: var(--script); font-weight: 700; }
  .serif { font-family: var(--serif); font-style: italic; font-weight: 700; }
  .brand {
    position: absolute; left: 0; right: 0; top: 1112px;
    display: flex; justify-content: center; align-items: center; gap: 12px;
    font-family: var(--condensed); font-size: 40px; color: var(--white);
  }
  .brand-dot { width: 30px; height: 30px; border-radius: 50%; background: var(--orange); }
</style>
</head>
<body>
<main class="poster">
  <div class="backdrop" role="img" aria-label="Night sky over a straight road stretching to the horizon through open desert"></div>

  <h1 class="title-banner">Nurse' Manifesto</h1>

  <!-- left column -->
  <p class="line" style="left:156px;top:131px;font-size:33px;letter-spacing:1px">Nurse with open hands,</p>
  <p class="line" style="left:156px;top:158px;font-size:36px;letter-spacing:1px">Hearts and minds</p>
  <p class="line small" style="left:156px;top:188px;font-size:13px">LOOK AFTER YOURSELF AND VALUE YOUR</p>
  <p class="line" style="left:154px;top:202px;font-size:78px;letter-spacing:4px">Health</p>
  <p class="line small" style="left:156px;top:270px;font-size:12px">AS MUCH AS YOU VALUE THE HEALTH OF OTHERS</p>
  <p class="line" style="left:156px;top:287px;font-size:46px;letter-spacing:2px">Learn</p>
  <p class="line serif" style="left:290px;top:282px;font-size:22px">Respect the limits of people's</p>
  <p class="line serif accent" style="left:290px;top:304px;font-size:44px">KNOWLEDGE</p>
  <p class="line serif" style="left:156px;top:325px;font-size:20px">something</p>
  <p class="line serif" style="left:156px;top:348px;font-size:18px">new each day</p>
  <p class="line small" style="left:290px;top:354px;font-size:11px">&amp; SHARE YOUR KNOWLEDGE GENEROUSLY</p>
  <p class="line small" style="left:156px;top:373px;font-size:10px">KNOWLEDGE &amp; SEEK ADVICE ONLY FROM REPUTED SOURCES</p>
  <p class="line script cream" style="left:210px;top:386px;font-size:19px">Be a lifelong</p>
  <p class="line" style="left:156px;top:404px;font-size:52px;letter-spacing:3px">Learner</p>
  <p class="line" style="left:156px;top:450px;font-size:36px;letter-spacing:1px">Celebrate, respect</p>
  <p class="line small" style="left:156px;top:485px;font-size:13px">AND VALUE THE DIVERSITY OF AUSTRALIAN CULTURE</p>
  <p class="line serif" style="left:152px;top:494px;font-size:96px">SMILE</p>
  <p class="line" style="left:156px;top:602px;font-size:30px;letter-spacing:1px">And infect others with your</p>
  <p class="line" style="left:156px;top:628px;font-size:34px;letter-spacing:1px">Happiness &amp; have fun!</p>
  <p class="line serif" style="left:156px;top:659px;font-size:24px">Always be solution focused</p>
  <p class="line" style="left:156px;top:693px;font-size:26px;letter-spacing:1px">Respone to complex situations</p>
  <p class="line serif" style="left:156px;top:715px;font-size:22px">Innovatively, Creatively</p>
  <p class="line small" style="left:156px;top:746px;font-size:11px">AND SAFELY WITHIN THE SCOPE OF YOUR PRACTICE</p>
  <p class="line" style="left:156px;top:762px;font-size:26px;letter-spacing:1px">Only follow</p>
  <p class="line" style="left:156px;top:784px;font-size:30px;letter-spacing:1px">Exceptional</p>
  <p class="line" style="left:156px;top:810px;font-size:34px;letter-spacing:1px">Leaders</p>
  <p class="line small" style="left:156px;top:852px;font-size:11px">ALWAYS LEAD WITH</p>
  <p class="line" style="left:156px;top:866px;font-size:46px;letter-spacing:2px">Purpose</p>
  <p class="line small" style="left:156px;top:906px;font-size:10px">PASSION &amp; COMMITMENT</p>
  <p class="line" style="left:156px;top:920px;font-size:32px;letter-spacing:1px">Adopt a 'can do'</p>
  <p class="line" style="left:156px;top:948px;font-size:54px;letter-spacing:2px">Attitude</p>
  <p class="line small" style="left:156px;top:996px;font-size:13px">TO EVERYTHING THAT</p>
  <p class="line small" style="left:156px;top:1014px;font-size:13px">COMES YOUR WAY</p>

  <!-- middle -->
  <p class="line small" style="left:300px;top:766px;font-size:12px">IF THERE IS NO ONE LEFT TO FOLLOW</p>
  <p class="line" style="left:300px;top:784px;font-size:52px;letter-spacing:1px">Then lead!</p>
  <p class="line small" style="left:300px;top:834px;font-size:12px">SEEK SUCCESS FIRSTLY FROM WITHIN</p>
  <p class="line serif" style="left:300px;top:850px;font-size:19px">Choose your thoughts wisely,</p>
  <p class="line serif" style="left:300px;top:874px;font-size:19px">they create your reality</p>
  <p class="line" style="left:334px;top:914px;font-size:60px;letter-spacing:2px">Live your</p>
  <p class="line" style="left:320px;top:958px;font-size:92px;letter-spacing:4px">Dream</p>

  <!-- right column -->
  <p class="line" style="left:538px;top:128px;font-size:56px;letter-spacing:1px">Deliver</p>
  <p class="line" style="left:538px;top:170px;font-size:66px;letter-spacing:2px">Care</p>
  <p class="line" style="left:538px;top:226px;font-size:37px;letter-spacing:1px">Skillfully.</p>
  <p class="line small" style="left:538px;top:380px;font-size:10px">SUPPORT YOUR COLLEAGUES AND</p>
  <p class="line" style="left:538px;top:394px;font-size:52px;letter-spacing:1px">Champion</p>
  <p class="line" style="left:538px;top:438px;font-size:24px">Their purpose.</p>
  <p class="line script accent" style="left:538px;top:456px;font-size:36px">Delight</p>
  <p class="line" style="left:538px;top:496px;font-size:32px">Your client and</p>
  <p class="line" style="left:538px;top:522px;font-size:32px">colleagues</p>
  <p class="line small" style="left:538px;top:552px;font-size:9px">BY EXCEEDING THEIR EXPECTATIONS</p>
  <p class="line" style="left:538px;top:566px;font-size:42px;letter-spacing:1px">You are</p>
  <p class="line" style="left:538px;top:600px;font-size:46px;letter-spacing:2px">Unique</p>
  <p class="line" style="left:538px;top:640px;font-size:24px">Revel in your</p>
  <p class="line" style="left:538px;top:660px;font-size:24px">individuality.</p>
  <p class="line" style="left:538px;top:684px;font-size:28px">Always do the</p>
  <p class="line script accent" style="left:560px;top:704px;font-size:40px">Right</p>
  <p class="line" style="left:538px;top:744px;font-size:26px">thing without</p>
  <p class="line" style="left:538px;top:766px;font-size:28px;letter-spacing:1px">exeption</p>

  <div class="brand"><span class="brand-dot"></span><span>CalmPath</span></div>
</main>
</body>
</html>
```